Business card design for web travel company

Hi
we'd like to receive some proposal for a business card design.
Stayvano is a private travel club, dedicated to all travel lovers, with unique offers for exclusive destinations all around the world. At Stayvano you can find a wide range of offers for resorts, boutique hotels and travel packages at the best guaranteed price available on the market. The convenience of the offer is guaranteed by a private sales model: offers are available for a limited time only and they are personally chosen by Stayvano's qualified team of travel experts.
We offer only exclusive hotels with discounted prices but we are not an outlet or a discount supermarket: the design should reflect our connection with luxury, exclusivity using the same style of our website www.stayvano-example.com.
We want to make sure that when we'll present ourself to our business partner they will feel immediately which is our brand positioning giving them also a sense of an affordable and reliable partner.
In attachment you can also find our brand guidelines (please note that we are NOT USING ANY MORE THE TAG LINE "Five star outlet" mentioned in it).
The info to be inserted are:
Name Surname
Job Title
Tel
Mobile (when needed)
Email
Stayvano S.r.l.
Via Bruno Lesta 27
20131 Milano

```html
<!DOCTYPE html>
<html lang="en">
<head>
<meta charset="utf-8">
<title>Stayvano business card</title>
<link rel="stylesheet" href="https://fonts.googleapis.com/css2?family=Arimo:wght@400;700&display=swap">
<style>
  :root {
    --bg: #ebe6dc;
    --card-white: #ffffff;
    --ink: #2b2925;
    --ink-soft: #55524c;
    --gold: #d5c49e;
    --card-dark: #2b2925;
    --on-dark: #ffffff;
  }
  * { margin: 0; padding: 0; box-sizing: border-box; }
  html, body { width: 1200px; height: 1200px; overflow: hidden; }
  body {
    background: var(--bg);
    font-family: "Arimo", Arial, sans-serif;
    color: var(--ink);
    position: relative;
  }
  .card {
    position: absolute;
    width: 792px;
    height: 486px;
    border-radius: 36px;
    overflow: hidden;
  }
  .card--front { left: 86px; top: 90px; background: var(--card-white); }
  .card--back { left: 314px; top: 624px; background: var(--card-dark); }

  .band { position: absolute; top: 178px; height: 90px; }
  .band--gold { left: 0; width: 72px; background: var(--gold); }
  .band--dark { left: 646px; width: 106px; background: var(--ink); }

  .wordmark {
    position: absolute;
    font-weight: 400;
    font-size: 104px;
    line-height: 1;
    letter-spacing: 1px;
    white-space: nowrap;
  }
  .card--front .wordmark { left: 92px; top: 170px; color: var(--ink); }
  .card--back .wordmark {
    left: 0; right: 0; top: 190px;
    text-align: center; color: var(--on-dark);
  }

  .contact { position: absolute; top: 336px; font-size: 22px; line-height: 1.3; color: var(--ink-soft); }
  .contact--person { left: 88px; }
  .contact--company { left: 387px; }
  .contact__name { font-weight: 700; color: var(--ink); font-size: 22px; margin-bottom: 2px; }
  .contact__role { font-size: 19px; }
  .contact__label { display: inline-block; width: 66px; }
</style>
</head>
<body>
  <section class="card card--front" aria-label="Business card front">
    <div class="band band--gold"></div>
    <div class="wordmark">Stayvano</div>
    <div class="band band--dark"></div>

    <div class="contact contact--person">
      <p class="contact__name">Stayvano</p>
      <p class="contact__role">Managing Director</p>
      <p>Mobile 123 456 7890</p>
    </div>
    <div class="contact contact--company">
      <p>Via Bruno Lesta 27 20131 Milano</p>
      <p><span class="contact__label">Tel</span>123 456 7890</p>
      <p>Email&nbsp; abcdefgh@stayvano-example.com</p>
    </div>
  </section>

  <section class="card card--back" aria-label="Business card back">
    <div class="wordmark">Stayvano</div>
  </section>
</body>
</html>
```